Business Card Design

New business card design

Target Market(s)

Residential & Commercial Property Managers

Industry/Entity Type

Plumbing Services

Contact Information for Business Card

Name - Owen Tredgold, title - Director, Phone Number - 0431 862 507, email - owen@rvb-plumbing.com.au, Company ABN - 73 215 904 386,

Font styles to use
Sans Serif

Colors
0054AA
0677BA
7BADD7
CADEEF
E8F1F8

```html
<!DOCTYPE html>
<html lang="en">
<head>
<meta charset="utf-8">
<title>RVB Plumbing Services – Business Card</title>
<link href="https://fonts.googleapis.com/css2?family=Poppins:wght@400;500;600&family=Michroma&display=swap" rel="stylesheet">
<style>
  :root {
    --backdrop: #b3b3b3;
    --card: #ffffff;
    --ink: #1d2329;
    --cyan: #00aeef;
    --navy-light: #0a78c0;
    --navy-mid: #0a5a9e;
    --navy-deep: #041a45;
    --splash-light: #7bc8f0;
    --splash-dark: #0a6a9a;
  }
  * { margin: 0; padding: 0; box-sizing: border-box; }
  html, body {
    width: 1200px; height: 1200px; overflow: hidden;
    background: var(--backdrop);
    font-family: "Poppins", sans-serif;
  }
  .card {
    position: absolute;
    top: 153px;
    width: 491px; height: 859px;
    background: var(--card);
    overflow: hidden;
  }
  .card--front { left: 88px; }
  .card--back  { left: 633px; }
  .card__art { position: absolute; inset: 0; width: 100%; height: 100%; }

  .brand {
    position: absolute; left: 0; right: 0;
    text-align: center;
    color: var(--ink);
    font-family: "Poppins", sans-serif;
    font-weight: 400;
  }
  .brand__name { display: block; line-height: 1; letter-spacing: 4px; }
  .brand__tag { display: block; letter-spacing: 0.9em; padding-left: 0.9em; }
  .card--front .brand { top: 92px; }
  .card--front .brand__name { font-size: 96px; }
  .card--front .brand__tag { font-size: 13px; margin-top: 34px; }
  .card--back .brand { top: 58px; }
  .card--back .brand__name { font-size: 64px; }
  .card--back .brand__tag { font-size: 9px; margin-top: 20px; }

  .person {
    position: absolute; top: 192px; left: 0; right: 0; text-align: center;
  }
  .person__name {
    font-family: "Michroma", sans-serif;
    font-size: 27px; letter-spacing: 0; color: var(--ink); white-space: nowrap;
  }
  .person__name span { color: var(--cyan); }
  .person__role {
    display: flex; align-items: center; justify-content: center; gap: 8px;
    margin-top: 2px; font-size: 18px; font-weight: 500; letter-spacing: 3px; color: var(--ink);
  }
  .person__role::before, .person__role::after {
    content: ""; width: 98px; height: 1px; background: var(--ink);
  }

  .contact { position: absolute; left: 0; right: 0; text-align: center; color: #111; }
  .contact__icon { display: block; margin: 0 auto 6px; }
  .contact__value { font-size: 22px; font-weight: 500; line-height: 1.1; }
  .contact--phone { top: 283px; }
  .contact--email { top: 380px; }
  .contact--abn { top: 476px; }
  .contact__label {
    font-size: 19px; font-weight: 600; letter-spacing: 4px; color: var(--cyan); line-height: 1.2;
  }
</style>
</head>
<body>

<section class="card card--front">
  <svg class="card__art" viewBox="0 0 491 859" aria-hidden="true">
    <defs>
      <linearGradient id="seaFront" x1="0" y1="0" x2="1" y2="0.3">
        <stop offset="0" stop-color="var(--navy-light)"/>
        <stop offset="0.6" stop-color="var(--navy-mid)"/>
        <stop offset="1" stop-color="var(--navy-deep)"/>
      </linearGradient>
      <linearGradient id="splashFront" x1="0" y1="0" x2="1" y2="1">
        <stop offset="0" stop-color="var(--splash-light)"/>
        <stop offset="1" stop-color="var(--splash-dark)"/>
      </linearGradient>
    </defs>
    <path d="M0,634 C110,612 200,650 280,705 C350,750 430,730 491,650 L491,859 L0,859 Z" fill="url(#seaFront)"/>
    <rect x="136" y="319" width="332" height="385" rx="60" fill="url(#splashFront)" opacity="0.55" role="img" aria-label="Water drop and splash illustration"/>
  </svg>
  <div class="brand">
    <span class="brand__name">rvb</span>
    <span class="brand__tag">plumbing services</span>
  </div>
</section>

<section class="card card--back">
  <svg class="card__art" viewBox="0 0 491 859" aria-hidden="true">
    <defs>
      <linearGradient id="seaBack" x1="0" y1="0" x2="1" y2="0.3">
        <stop offset="0" stop-color="var(--navy-light)"/>
        <stop offset="0.6" stop-color="var(--navy-mid)"/>
        <stop offset="1" stop-color="var(--navy-deep)"/>
      </linearGradient>
      <linearGradient id="splashBack" x1="0" y1="0" x2="1" y2="1">
        <stop offset="0" stop-color="var(--splash-light)"/>
        <stop offset="1" stop-color="var(--splash-dark)"/>
      </linearGradient>
    </defs>
    <path d="M0,700 C100,672 200,705 290,758 C360,800 445,792 491,728 L491,859 L0,859 Z" fill="url(#seaBack)"/>
    <rect x="283" y="543" width="188" height="223" rx="40" fill="url(#splashBack)" opacity="0.55" role="img" aria-label="Water drop and splash illustration"/>
  </svg>

  <div class="brand">
    <span class="brand__name">rvb</span>
    <span class="brand__tag">plumbing services</span>
  </div>

  <div class="person">
    <h1 class="person__name">OWEN <span>TREDGOLD</span></h1>
    <p class="person__role">Director</p>
  </div>

  <div class="contact contact--phone">
    <svg class="contact__icon" width="30" height="42" viewBox="0 0 30 42" aria-hidden="true">
      <path d="M15 2 C10 10 3 17 3 27 A12 12 0 0 0 27 27 C27 17 20 10 15 2 Z" fill="#fff" stroke="var(--cyan)" stroke-width="2.5"/>
      <path d="M15 2 L10 11 L20 11 Z" fill="var(--cyan)"/>
      <path d="M11 22 l2.5-1.5 2 3 -1.5 1 c0.8 1.8 1.8 2.8 3.5 3.5 l1-1.5 3 2 -1.5 2.5 c-4.5 0-9-4.5-9-9 z" fill="var(--ink)"/>
    </svg>
    <p class="contact__value">0431 862 507</p>
  </div>

  <div class="contact contact--email">
    <svg class="contact__icon" width="30" height="42" viewBox="0 0 30 42" aria-hidden="true">
      <path d="M15 2 C10 10 3 17 3 27 A12 12 0 0 0 27 27 C27 17 20 10 15 2 Z" fill="#fff" stroke="var(--cyan)" stroke-width="2.5"/>
      <path d="M15 2 L10 11 L20 11 Z" fill="var(--cyan)"/>
      <rect x="8.5" y="23" width="13" height="9" fill="var(--ink)"/>
      <path d="M8.5 23 L15 28 L21.5 23" fill="none" stroke="#fff" stroke-width="1"/>
    </svg>
    <p class="contact__value">owen@rvb-plumbing.com.au</p>
  </div>

  <div class="contact contact--abn">
    <p class="contact__label">Company ABN</p>
    <p class="contact__value">73 215 904 386</p>
  </div>
</section>

</body>
</html>
```